Business Card for Bright Furrow Lawn & Landscape

Double Sided Card Design - I think one side of the card should be cleaner, with logo, contact info, and "Complete Residential & Commercial Landscape Services", and on the other side it should list the services we offer:

- Lawn Care & Mowing
- Hedge & Shrub Trimming
- Leaf Removal & Clean Up
- Aeration & Sod
- Mulch & Rock Installations
- Landscape Installations & Renovations
- Commercial Snow Removal

Please make it clean and very professional... don't want it too be too busy, but want to tell them what we do.

Target Market(s)

Residential and Commercial

Industry/Entity Type

Landscape

Contact Information for Business Card

Fully Insured
Dale Ostrov
410-372-6184
Dostrov07@quillpost.net

Requirements
Must have
• Double Sided, Cleaner on one side, more information and text on the other side.

```html
<!DOCTYPE html>
<html lang="en">
<head>
<meta charset="utf-8">
<title>Bright Furrow Lawn &amp; Landscape – Business Card</title>
<link rel="stylesheet" href="https://fonts.googleapis.com/css2?family=Cinzel:wght@600;700&family=Lora:wght@400;500&display=swap">
<style>
  :root {
    --green: #8bbb3f;
    --green-soft: #b5d67d;
    --ink: #111111;
    --paper: #ffffff;
    --stage: #e9eae6;
    --title-font: "Cinzel", "Times New Roman", serif;
    --body-font: "Lora", Georgia, serif;
  }
  * { margin: 0; padding: 0; box-sizing: border-box; }
  html, body { width: 1200px; height: 1189px; overflow: hidden; background: var(--stage); }
  .canvas { position: relative; width: 1200px; height: 1189px; }

  .card {
    position: absolute; left: 150px; width: 900px; height: 514px;
    border-radius: 28px; overflow: hidden;
    box-shadow: 0 10px 30px rgba(0,0,0,.18);
  }

  /* ---------- Front ---------- */
  .card-front { top: 52px; background: var(--paper); }
  .front-grass { position: absolute; }
  .front-grass--left { left: 40px; bottom: 60px; width: 260px; height: 220px; }
  .front-grass--right { right: 30px; bottom: 100px; width: 280px; height: 150px; }
  .front-band {
    position: absolute; left: 0; right: 0; bottom: 0; height: 108px;
    background: var(--green);
    display: flex; align-items: center; justify-content: center;
  }
  .tagline { font-family: var(--body-font); font-size: 25px; color: var(--ink); letter-spacing: .3px; }

  .brand-front { position: absolute; top: 58px; left: 0; right: 0; text-align: center; }
  .brand-mark {
    display: inline-block; width: 96px; height: 96px; border-radius: 50%;
    border: 10px solid var(--green); margin-bottom: 14px;
  }
  .brand-name {
    font-family: var(--title-font); font-weight: 700; color: var(--green);
    font-size: 50px; line-height: 1; letter-spacing: 1px;
  }
  .brand-sub {
    font-family: var(--title-font); font-weight: 600; color: var(--ink);
    font-size: 20px; letter-spacing: 11px; margin-top: 8px;
  }
  .contact { position: absolute; top: 290px; left: 0; right: 0; text-align: center; }
  .contact-name {
    font-family: var(--title-font); font-weight: 600; font-size: 24px;
    letter-spacing: 1.5px; color: var(--ink);
  }
  .contact-line { font-family: var(--body-font); font-size: 19px; color: var(--ink); margin-top: 6px; }
  .contact-label { color: var(--green); font-weight: 500; }
  .contact-sep { margin: 0 8px; }

  /* ---------- Back ---------- */
  .card-back { top: 620px; background: var(--ink); }
  .back-panel { position: absolute; top: 0; right: 0; width: 380px; height: 514px; }
  .back-emblem {
    position: absolute; left: 540px; top: 80px; width: 340px; height: 340px;
    border-radius: 50%; background: var(--paper);
    display: flex; align-items: center; justify-content: center;
    flex-direction: column; text-align: center;
  }
  .back-emblem .brand-name { font-size: 40px; color: var(--ink); }

  .brand-back { position: absolute; left: 62px; top: 58px; }
  .brand-back .brand-name { font-size: 54px; }
  .brand-back .brand-sub { color: var(--paper); font-size: 21px; letter-spacing: 12px; }

  .services { position: absolute; left: 62px; top: 210px; }
  .services-title {
    font-family: var(--title-font); font-weight: 700; color: var(--green);
    font-size: 26px; letter-spacing: 1px; margin-bottom: 14px;
  }
  .services-list { list-style: none; }
  .services-list li {
    font-family: var(--body-font); color: var(--paper); font-size: 22px;
    line-height: 33px; padding-left: 30px; position: relative;
  }
  .services-list li::before {
    content: ""; position: absolute; left: 2px; top: 13px;
    width: 9px; height: 9px; border-radius: 50%; background: var(--green);
  }
</style>
</head>
<body>
<main class="canvas">

  <section class="card card-front" aria-label="Card front">
    <svg class="front-grass front-grass--left" role="img" aria-label="Green grass blades illustration" viewBox="0 0 260 220">
      <defs><linearGradient id="grassL" x1="0" y1="1" x2="0" y2="0"><stop offset="0" stop-color="#8bbb3f"/><stop offset="1" stop-color="#8bbb3f" stop-opacity="0"/></linearGradient></defs>
      <rect width="260" height="220" rx="40" fill="url(#grassL)"/>
    </svg>
    <svg class="front-grass front-grass--right" role="img" aria-label="Green grass blades illustration" viewBox="0 0 280 150">
      <defs><linearGradient id="grassR" x1="0" y1="1" x2="0" y2="0"><stop offset="0" stop-color="#8bbb3f"/><stop offset="1" stop-color="#8bbb3f" stop-opacity="0"/></linearGradient></defs>
      <rect width="280" height="150" rx="40" fill="url(#grassR)"/>
    </svg>

    <div class="brand-front">
      <span class="brand-mark"></span>
      <div class="brand-name">Bright Furrow</div>
      <div class="brand-sub">LAWN &amp; LANDSCAPE</div>
    </div>

    <div class="contact">
      <div class="contact-name">Dale Ostrov</div>
      <div class="contact-line"><span class="contact-label">P:</span> 410-372-6184<span class="contact-sep">|</span><span class="contact-label">E:</span> Dostrov07@quillpost.net</div>
    </div>

    <div class="front-band"><p class="tagline">Complete Residential &amp; Commercial Landscape Services</p></div>
  </section>

  <section class="card card-back" aria-label="Card back">
    <svg class="back-panel" viewBox="0 0 380 514" aria-hidden="true">
      <polygon points="80,0 380,0 380,514 240,514" fill="#8bbb3f"/>
    </svg>
    <div class="back-emblem">
      <div class="brand-name">Bright Furrow</div>
    </div>

    <div class="brand-back">
      <div class="brand-name">Bright Furrow</div>
      <div class="brand-sub">LAWN &amp; LANDSCAPE</div>
    </div>

    <div class="services">
      <h2 class="services-title">Services We Offer</h2>
      <ul class="services-list">
        <li>Lawn Care &amp; Mowing</li>
        <li>Hedge &amp; Shrub Trimming</li>
        <li>Leaf Removal &amp; Clean Up</li>
        <li>Aeration &amp; Sod</li>
        <li>Mulch &amp; Rock Installations</li>
        <li>Landscape Installations &amp; Renovations</li>
        <li>Commercial Snow Removal</li>
      </ul>
    </div>
  </section>

</main>
</body>
</html>
```